Under the Willow Painters & Decorators

Make your dreams come true. 30 Years experience , Domestic & Commercial , Interior & Exterior , For free Advice & Quotes Call Neville 03 96248107 or 0412586230 Email willowdecorators@fernmail.example

Industry/Entity Type

Painting And Decorating

Contact Information for Business Card

Under The Willow Painters & Decorators Neville Purdom

Requirements
Must have
• Rainbow theme with a touch of irish
Nice to have
• maybe a leprechaun in white overalls painting the rainbow with the logo Make your dreams come true.

```html
<!DOCTYPE html>
<html lang="en">
<head>
<meta charset="utf-8">
<title>Under the Willow Painters &amp; Decorators – Business Card</title>
<link rel="stylesheet" href="https://fonts.googleapis.com/css2?family=Italianno&family=Tinos&display=swap">
<style>
  :root {
    --navy: #1b2180;
    --purple: #5a1f8f;
    --bullet: #b13fd8;
    --red: #e3213c;
    --white: #ffffff;
    --green: #2fc43a;
    --irish-green: #169b62;
    --irish-orange: #ff883e;
    --yellow: #ffd21a;
    --orange: #ff7a12;
    --crimson: #d8142c;
    --magenta: #ff1fb4;
    --blue: #1f7fe0;
  }
  html, body {
    margin: 0;
    padding: 0;
    width: 1200px;
    height: 721px;
    overflow: hidden;
    background: var(--white);
  }
  .card {
    position: relative;
    width: 1200px;
    height: 721px;
    overflow: hidden;
    background: var(--white);
    font-family: "Tinos", "Times New Roman", serif;
  }
  .card__swirls {
    position: absolute;
    inset: 0;
    width: 1200px;
    height: 721px;
  }
  .card__text {
    position: absolute;
    margin: 0;
    white-space: nowrap;
    line-height: 1;
  }
  .brand-name {
    left: 0;
    width: 1200px;
    text-align: center;
    top: 212px;
    font-family: "Italianno", cursive;
    font-size: 104px;
    font-weight: 400;
    color: var(--navy);
    padding-left: 4px;
  }
  .brand-trade {
    left: 0;
    width: 1188px;
    text-align: center;
    top: 304px;
    font-size: 44px;
    color: var(--navy);
  }
  .feature {
    font-size: 32px;
    letter-spacing: 2.6px;
    color: var(--purple);
  }
  .feature::before {
    content: "";
    display: inline-block;
    width: 9px;
    height: 9px;
    margin-right: 3px;
    border-radius: 50%;
    background: var(--bullet);
    vertical-align: middle;
    position: relative;
    top: -3px;
  }
  .feature--experience { left: 196px; top: 373px; }
  .feature--standard   { left: 613px; top: 373px; }
  .feature--location   { left: 177px; top: 418px; }
  .feature--sector     { left: 578px; top: 418px; }
  .tagline {
    left: 0;
    width: 1188px;
    text-align: center;
    top: 468px;
    font-family: "Italianno", cursive;
    font-size: 62px;
    color: var(--navy);
  }
  .contact {
    right: 21px;
    text-align: right;
    color: var(--red);
  }
  .contact--name    { top: 520px; font-size: 42px; }
  .contact--address { top: 582px; font-size: 27px; }
  .contact--phone   { top: 632px; font-size: 27px; }
  .contact--email   { top: 684px; font-size: 27px; }
</style>
</head>
<body>
<main class="card">
  <svg class="card__swirls" viewBox="0 0 1200 721" role="img" aria-label="Rainbow paint swirls with an Irish green edge and pink paint drips framing the card">
    <defs>
      <linearGradient id="rainbow-sweep" x1="0" y1="1" x2="1" y2="0">
        <stop offset="0" stop-color="var(--blue)"/>
        <stop offset="0.22" stop-color="var(--irish-green)"/>
        <stop offset="0.32" stop-color="var(--green)"/>
        <stop offset="0.44" stop-color="var(--yellow)"/>
        <stop offset="0.56" stop-color="var(--orange)"/>
        <stop offset="0.68" stop-color="var(--crimson)"/>
        <stop offset="0.85" stop-color="var(--magenta)"/>
        <stop offset="1" stop-color="var(--magenta)"/>
      </linearGradient>
    </defs>
    <rect width="1200" height="721" fill="url(#rainbow-sweep)"/>
    <path d="M100 721 C 70 560, 110 330, 300 220 C 470 120, 760 110, 960 150 C 1080 175, 1160 220, 1200 250 L 1200 721 Z" fill="var(--white)"/>
    <path class="irish-band" d="M100 721 C 70 560, 110 330, 300 220 C 470 120, 760 110, 960 150 C 1080 175, 1160 220, 1200 250" fill="none" stroke="var(--irish-green)" stroke-width="10"/>
    <path class="irish-band" d="M116 721 C 86 562, 124 340, 308 234 C 474 136, 760 126, 956 166 C 1074 190, 1154 234, 1200 264" fill="none" stroke="var(--irish-orange)" stroke-width="4"/>
  </svg>

  <h1 class="card__text brand-name">Under the Willow</h1>
  <p class="card__text brand-trade">Painters &amp; Decorators</p>

  <p class="card__text feature feature--experience">30 years of experience</p>
  <p class="card__text feature feature--standard">A high work standard</p>
  <p class="card__text feature feature--location">Interior &amp; Exterior</p>
  <p class="card__text feature feature--sector">Domestic &amp; Commercial</p>

  <p class="card__text tagline">We’ll make your dreams come true</p>

  <p class="card__text contact contact--name">Neville Purdom</p>
  <p class="card__text contact contact--address">48 Kestrel Lane Ardenvale 3391</p>
  <p class="card__text contact contact--phone">03 96248107 or 0412586230</p>
  <p class="card__text contact contact--email">Email willowdecorators@fernmail.example</p>
</main>
</body>
</html>
```